Swept Breeze Icons

Icons we would like submitted:

Home
Menu
Shop
Members
Contact
Join the team
Classes
Specials
On the go
Parties

I want simple and sleek there is a company called fern and comb in Houston Texas, we really love their icons, these are good examples. We like the outline look these have. We are also a blow dry bar - NO SCISSORS, NO COLOR APPLICATION, JUST BLOW DRYS AND ALCOHOL.

Please feel free to be excited creative and fun!!
Updates

As soon as I get submissions I will give feedback and accept as soon as I am happy.

Target Market(s)

high end women

Industry/Entity Type

It Company

Requirements
Must have
• cute
Should not have
• succors

```html
<!DOCTYPE html>
<html lang="en">
<head>
<meta charset="utf-8">
<title>Swept Breeze Blow Dry Bar</title>
<link rel="stylesheet" href="https://fonts.googleapis.com/css2?family=Open+Sans:wght@400;600;700&display=swap">
<style>
  :root {
    --frame-grey: #6d6d6f;
    --teal: #4cbfcd;
    --teal-dark: #3aaab8;
    --pink: #d96fd8;
    --white: #ffffff;
    --subtitle-grey: #4a4a4c;
    --wall-top: #5b5251;
    --wall-bottom: #3d3b3e;
    --social-a: #8cb36a;
    --social-b: #3b5b9a;
    --social-c: #8a7a6a;
  }
  html, body {
    margin: 0;
    padding: 0;
    width: 1200px;
    height: 797px;
    overflow: hidden;
    background: var(--frame-grey);
    font-family: "Open Sans", Arial, sans-serif;
  }
  .site {
    position: relative;
    width: 1200px;
    height: 797px;
    background: var(--frame-grey);
  }
  .brand {
    position: absolute;
    top: 58px;
    left: 0;
    width: 1200px;
    text-align: center;
  }
  .brand-name {
    display: inline-flex;
    align-items: center;
    gap: 14px;
    font-size: 60px;
    font-weight: 700;
    color: var(--teal);
    line-height: 1;
    letter-spacing: -1px;
  }
  .brand-dot {
    width: 22px;
    height: 22px;
    border-radius: 50%;
    background: var(--teal);
  }
  .brand-tagline {
    margin-top: 4px;
    font-size: 22px;
    color: var(--subtitle-grey);
    letter-spacing: 0.5px;
  }
  .social {
    position: absolute;
    top: 24px;
    right: 40px;
    display: flex;
    gap: 6px;
  }
  .social-square {
    width: 36px;
    height: 36px;
    border-radius: 6px;
  }
  .social-square.a { background: var(--social-a); }
  .social-square.b { background: var(--social-b); }
  .social-square.c { background: var(--social-c); }
  .header-rule {
    position: absolute;
    top: 176px;
    left: 36px;
    right: 60px;
    height: 2px;
    background: var(--teal);
  }
  .main-nav {
    position: absolute;
    top: 196px;
    left: 24px;
    right: 24px;
    height: 108px;
    background: var(--teal);
  }
  .nav-list {
    list-style: none;
    margin: 0;
    padding: 0 0 0 130px;
    display: flex;
    height: 100%;
  }
  .nav-item {
    display: flex;
    flex-direction: column;
    align-items: center;
    justify-content: center;
    padding: 0 12px;
    color: var(--white);
    font-size: 17px;
    font-weight: 600;
    white-space: nowrap;
  }
  .nav-item svg {
    width: 46px;
    height: 46px;
    margin-bottom: 6px;
  }
  .nav-item.is-active {
    background: var(--pink);
    width: 72px;
    font-weight: 700;
  }
  .content {
    position: absolute;
    top: 304px;
    left: 24px;
    right: 24px;
    height: 452px;
    background: linear-gradient(160deg, var(--wall-top), var(--wall-bottom));
  }
  .photo {
    position: absolute;
  }
  .photo-group {
    left: 206px;
    top: 30px;
    width: 220px;
    height: 238px;
    background: linear-gradient(180deg, #c9b08f, #8c7a5a);
  }
  .photo-hair {
    left: 780px;
    top: 236px;
    width: 214px;
    height: 190px;
    background: linear-gradient(90deg, #e9e4dc, #c79a6a);
  }
  .copy {
    position: absolute;
    margin: 0;
    color: var(--white);
    font-size: 15px;
    font-weight: 600;
    line-height: 20px;
    text-align: center;
    text-shadow: 0 1px 2px #000;
  }
  .copy-top {
    left: 440px;
    top: 22px;
    width: 520px;
  }
  .copy-bottom {
    left: 250px;
    top: 318px;
    width: 510px;
  }
</style>
</head>
<body>
<div class="site">
  <header>
    <div class="brand">
      <div class="brand-name"><span>Swept Breeze</span><span class="brand-dot"></span></div>
      <div class="brand-tagline">Blow Dry Bar</div>
    </div>
    <div class="social" aria-label="Social links">
      <span class="social-square a"></span>
      <span class="social-square b"></span>
      <span class="social-square c"></span>
    </div>
    <div class="header-rule"></div>
  </header>

  <nav class="main-nav">
    <ul class="nav-list">
      <li class="nav-item is-active">
        <svg viewBox="0 0 40 40" fill="#fff"><path d="M20 6 L4 20 H9 V34 H17 V25 H23 V34 H31 V20 H36 Z"/></svg>
        Home
      </li>
      <li class="nav-item">
        <svg viewBox="0 0 40 40" fill="#fff"><rect x="4" y="8" width="24" height="12" rx="6"/><rect x="28" y="9" width="6" height="10" rx="1"/><rect x="10" y="18" width="7" height="16" rx="2"/></svg>
        Menu
      </li>
      <li class="nav-item">
        <svg viewBox="0 0 40 40" fill="none" stroke="#fff" stroke-width="2.5"><rect x="6" y="16" width="28" height="18"/><rect x="4" y="11" width="32" height="6"/><path d="M20 11 V34"/><path d="M20 11 C14 2 8 8 20 11 C32 8 26 2 20 11"/></svg>
        Shop
      </li>
      <li class="nav-item">
        <svg viewBox="0 0 40 40" fill="#fff"><path d="M2 20 C8 10 15 9 20 13 C25 9 32 10 38 20 C30 31 10 31 2 20 Z"/><path d="M5 20 C14 22 26 22 35 20" stroke="#4cbfcd" stroke-width="2" fill="none"/></svg>
        Members
      </li>
      <li class="nav-item">
        <svg viewBox="0 0 40 40" fill="none" stroke="#fff" stroke-width="2.5"><rect x="11" y="3" width="18" height="34" rx="3"/><path d="M17 32 H23"/><path d="M20 22 L15 17 A3 3 0 0 1 20 13 A3 3 0 0 1 25 17 Z" fill="#fff" stroke="none"/></svg>
        Contact
      </li>
      <li class="nav-item">
        <svg viewBox="0 0 40 40" fill="#fff"><circle cx="20" cy="11" r="5"/><path d="M12 30 C12 20 28 20 28 30 Z"/><circle cx="9" cy="15" r="4"/><path d="M2 31 C2 23 14 22 14 28 Z"/><circle cx="31" cy="15" r="4"/><path d="M38 31 C38 23 26 22 26 28 Z"/></svg>
        Join the team
      </li>
      <li class="nav-item">
        <svg viewBox="0 0 40 40" fill="none" stroke="#fff" stroke-width="2.5"><circle cx="20" cy="15" r="10"/><path d="M20 25 V31 M12 35 H28"/></svg>
        Classes
      </li>
      <li class="nav-item">
        <svg viewBox="0 0 40 40" fill="none" stroke="#fff" stroke-width="2.5" stroke-linejoin="round"><path d="M20 16 L5 8 V24 Z M20 16 L35 8 V24 Z"/><path d="M18 18 L10 34 M22 18 L30 34"/></svg>
        Specials
      </li>
      <li class="nav-item">
        <svg viewBox="0 0 40 40" fill="#fff"><path d="M4 26 V20 C4 17 6 16 9 15 L13 8 C14 7 15 6 17 6 H25 C27 6 28 7 29 8 L32 15 C35 16 36 17 36 20 V26 Z"/><circle cx="11" cy="28" r="4"/><circle cx="29" cy="28" r="4"/><path d="M14 14 L16 9 H24 L26 14 Z" fill="#4cbfcd"/></svg>
        On the go
      </li>
      <li class="nav-item">
        <svg viewBox="0 0 40 40" fill="#fff"><rect x="8" y="4" width="5" height="7"/><path d="M6 14 C6 11 15 11 15 14 V36 H6 Z"/><path d="M21 14 H35 L32 26 H24 Z"/><rect x="27" y="26" width="2" height="8"/><rect x="23" y="34" width="10" height="2"/></svg>
        Parties
      </li>
    </ul>
  </nav>

  <main class="content" role="img" aria-label="Weathered brick wall background">
    <div class="photo photo-group" role="img" aria-label="Photo of four women standing together outdoors"></div>
    <div class="photo photo-hair" role="img" aria-label="Photo of long wavy blonde hair"></div>
    <p class="copy copy-top">Lorem ipsum dolor sit amet, consectetur adipiscing elit. Aenean est orci, aliquam in erat dignissim, lobortis rutrum enim. Nam et enim nec libero iaculis faucibus et vitae erat. Maecenas nunc eros, vestibulum ut purus quis, hendrerit imperdiet nulla. Praesent eros ligula, auctor at rutrum quis, scelerisque eu diam. Nam efficitur felis et turpis dapibus, id ultrices est accumsan. Donec non eros mattis, rutrum nisl sed, luctus ligula. Vestibulum iaculis bibendum nulla, et mollis ligula elementum sit amet. Phasellus sollicitudin gravida nisl, id vulputate arcu. Nulla non enim dolor, sce. Ultrices nisl nunc, non accumsan augue.</p>
    <p class="copy copy-bottom">Lorem ipsum dolor sit amet, consectetur adipiscing elit. Aenean est orci, aliquam in erat dignissim, lobortis rutrum enim. Nam et enim nec libero iaculis faucibus et vitae erat. Maecenas nunc eros, vestibulum ut purus quis, hendrerit imperdiet nulla. Praesent eros ligula, auctor at rutrum quis, scelerisque eu diam. Nam efficitur felis et turpis dapibus, id ultrices est accumsan.</p>
  </main>
</div>
</body>
</html>
```